Stand out flyer needed for Boxing gym

Hi we need a trifold brochure designed for our outdoor boxing business it will be delivered to doctors and nutritionists to help their patients be healthier and get fit.We have supplied high res pictures for you to use in the brochure. We need a design that use a lot of yellow so it captures their attention. You can check our website for design colours www.punchyard-fit.com.au

Target Market(s)

Overweight or unfit people looking to change their lives

Industry/Entity Type

Health And Wellness

Font styles to use
Sans Serif

Colors
fbee3d
ffffff
000000

Requirements
Must have
• (main heading - large bold font) Get fit lose weight & feel great
• (bold) Unlimited outdoor boxing classes $14.95
• Complete affordability & No judgements guaranteed
• (bold) Tailored programs (bold)
• Our programs are structured so that members of all fitness levels feel confident & comfortable during their start-up phase allowing you to quickly build your fitness
• (bold) Injury prevention (bold)
• Our training systems include techniques that will help you avoid injuries and build balanced strength
• (bold) Strengthen & Tone your core (bold)
• You're core muscles are some of you're most important muscles. Each workout you do incorporates core exercises to help avoid injuries and make you're total body stronger
• (bold) Wake up with more energy(bold)
• Every class you'll do will have you filled with energy the will pump you up for the rest of your day
• (bold) Sleep better(bold)
• One of the best parts of exercise is the benefit it has on your sleeping patterns. You'll sleep deeper & more sound
• (bold) Supportive environment (bold)
• At JAB YARD you'll be surrounded by trainers & other members who are there to encourage & motivate you to reach your goals and to get you moving more.
• Coupon code: SwingHigh27

```html
<!DOCTYPE html>
<html lang="en">
<head>
<meta charset="utf-8">
<title>JAB YARD trifold brochure</title>
<link href="https://fonts.googleapis.com/css2?family=Oswald:wght@400;500;600&family=Open+Sans:wght@400;600&display=swap" rel="stylesheet">
<style>
  :root {
    --yellow: #fbc813;
    --yellow-bright: #fbee3d;
    --gold: #d9a400;
    --black: #0b0b0b;
    --white: #ffffff;
    --ink: #2a2a2a;
    --canvas: #eeedee;
  }
  * { box-sizing: border-box; margin: 0; padding: 0; }
  html, body { width: 880px; height: 1200px; overflow: hidden; }
  body { background: var(--canvas); font-family: "Open Sans", Arial, sans-serif; position: relative; }

  .spread { position: absolute; left: 40px; width: 800px; height: 564px; background: var(--white); overflow: hidden; box-shadow: 0 4px 12px rgba(0,0,0,.18); }
  .spread--outside { top: 24px; }
  .spread--inside { top: 612px; }

  .panel { position: absolute; top: 0; width: 266.67px; height: 564px; overflow: hidden; }
  .panel--1 { left: 0; }
  .panel--2 { left: 266.67px; }
  .panel--3 { left: 533.33px; }

  .photo { position: absolute; }
  .overlay { position: absolute; left: 0; top: 0; }

  .feature { position: absolute; left: 14px; right: 14px; text-align: center; }
  .icon { width: 34px; height: 34px; display: block; margin: 0 auto 6px; }
  .feature__title { font-family: "Oswald", Arial, sans-serif; font-weight: 500; font-size: 15px; text-transform: uppercase; color: var(--gold); letter-spacing: .2px; margin-bottom: 8px; }
  .feature__text { font-size: 8.6px; line-height: 1.38; text-align: justify; color: var(--ink); }
  .on-dark .feature__title, .on-yellow .feature__title { color: var(--yellow); }
  .on-dark .feature__text { color: #e6e6e6; }
  .on-yellow .feature__title { color: var(--black); }
  .on-yellow .feature__text { color: #3a2e00; }

  .brand { font-family: "Oswald", Arial, sans-serif; font-weight: 500; text-align: center; letter-spacing: 3px; }
  .brand--back { position: absolute; left: 0; right: 0; top: 245px; font-size: 30px; color: var(--white); }
  .brand--cover { position: absolute; left: 0; right: 0; top: 18px; font-size: 38px; color: var(--black); }

  .contact { position: absolute; left: 0; right: 0; text-align: center; font-size: 9.5px; font-weight: 600; }
  .contact__line { display: flex; flex-direction: column; align-items: center; margin-bottom: 8px; }
  .contact__line svg { width: 12px; height: 12px; margin-bottom: 3px; }
  .contact__cta { font-family: "Oswald", Arial, sans-serif; font-weight: 500; font-size: 15px; color: var(--yellow); line-height: 1.3; margin-bottom: 18px; text-transform: uppercase; }
  .contact--back { top: 325px; color: var(--white); }
  .contact--inside { top: 412px; color: var(--ink); }

  .cover-heading { position: absolute; left: 0; right: 0; top: 110px; text-align: center; font-family: "Oswald", Arial, sans-serif; font-weight: 600; font-size: 25px; line-height: 1.15; text-transform: uppercase; color: var(--black); }
  .cover-heading span { color: var(--white); }
  .price-bar { position: absolute; left: 18px; right: 18px; top: 178px; background: var(--black); border: 1px solid var(--white); color: var(--white); font-family: "Oswald", Arial, sans-serif; font-weight: 500; font-size: 12px; text-align: center; padding: 2px 0; text-transform: uppercase; }
  .price-bar span { color: var(--yellow); }
  .tagline { position: absolute; left: 0; right: 0; top: 204px; text-align: center; font-size: 8px; color: var(--black); }
  .web { position: absolute; left: 0; right: 0; bottom: 18px; text-align: center; font-size: 9px; letter-spacing: 2px; color: var(--ink); font-weight: 600; }

  .badge { position: absolute; left: 565px; top: 190px; width: 130px; height: 130px; border-radius: 50%; background: var(--yellow); border: 3px solid var(--black); box-shadow: 0 0 0 3px var(--yellow); display: flex; align-items: center; justify-content: center; text-align: center; font-family: "Oswald", Arial, sans-serif; font-weight: 500; font-size: 18px; line-height: 1.1; text-transform: uppercase; color: var(--black); }
</style>
</head>
<body>

<!-- Outside of the trifold -->
<section class="spread spread--outside">

  <div class="panel panel--1">
    <div class="photo" role="img" aria-label="Black and white photo of a female boxer in guard stance with wraps" style="left:0;top:290px;width:267px;height:274px;background:radial-gradient(ellipse at 45% 55%,#6a6a6a 0%,#2c2c2c 45%,#0d0d0d 80%);"></div>
    <svg class="overlay" width="267" height="564" viewBox="0 0 267 564">
      <path d="M0,0 H267 V300 C210,292 120,300 0,395 Z" fill="#ffffff"/>
      <path d="M0,395 C120,300 210,292 267,300 V316 C205,306 125,318 0,412 Z" fill="#fbc813"/>
    </svg>
    <div class="feature" style="top:22px;">
      <svg class="icon" viewBox="0 0 34 34"><circle cx="17" cy="17" r="15.5" fill="none" stroke="#d9a400" stroke-width="2"/><circle cx="17" cy="11" r="3" fill="#d9a400"/><path d="M10,17 H24 M17,14 V24 M12,25 H22" stroke="#d9a400" stroke-width="2" fill="none"/></svg>
      <h3 class="feature__title">Tailored programs</h3>
      <p class="feature__text">Our programs are structured so that members of all fitness levels feel confident &amp; comfortable during their start-up phase allowing you to quickly build your fitness</p>
    </div>
    <div class="feature" style="top:178px;">
      <svg class="icon" viewBox="0 0 34 34"><circle cx="17" cy="17" r="15.5" fill="none" stroke="#d9a400" stroke-width="2"/><path d="M9,22 L17,14 L25,22 M17,14 V10" stroke="#d9a400" stroke-width="2" fill="none"/><circle cx="17" cy="8.5" r="2" fill="#d9a400"/></svg>
      <h3 class="feature__title">Injury prevention</h3>
      <p class="feature__text">Our training systems include techniques that will help you avoid injuries and build balanced strength</p>
    </div>
  </div>

  <div class="panel panel--2 on-dark" style="background:var(--black);">
    <div class="photo" role="img" aria-label="Faint dark photo of a hooded boxer" style="left:0;top:0;width:267px;height:564px;background:radial-gradient(ellipse at 50% 30%,#262626 0%,#111 55%,#070707 100%);"></div>
    <div class="brand brand--back">JAB YARD</div>
    <div class="contact contact--back">
      <p class="contact__cta">Contact us today<br>for more information</p>
      <div class="contact__line"><svg viewBox="0 0 12 12"><circle cx="6" cy="6" r="5.2" fill="none" stroke="#fbc813" stroke-width="1.2"/><path d="M4,3.5 L5,3.5 L5.5,5 L4.8,5.6 C5.3,6.6 5.9,7.2 6.8,7.6 L7.4,6.9 L8.7,7.4 L8.5,8.5 C6,8.5 3.6,6 4,3.5 Z" fill="#fbc813"/></svg>0400 123 987</div>
      <div class="contact__line"><svg viewBox="0 0 12 12"><rect x="1.5" y="3" width="9" height="6" fill="none" stroke="#fbc813" stroke-width="1.1"/><path d="M1.5,3 L6,6.5 L10.5,3" fill="none" stroke="#fbc813" stroke-width="1.1"/></svg>info@punchyard-fit.com.au</div>
      <div class="contact__line"><svg viewBox="0 0 12 12"><circle cx="6" cy="6" r="4.8" fill="none" stroke="#fbc813" stroke-width="1.1"/><path d="M1.2,6 H10.8 M6,1.2 C3.8,4 3.8,8 6,10.8 M6,1.2 C8.2,4 8.2,8 6,10.8" fill="none" stroke="#fbc813" stroke-width="0.9"/></svg>www.punchyard-fit.com.au</div>
    </div>
  </div>

  <div class="panel panel--3" style="background:var(--yellow);">
    <div class="photo" role="img" aria-label="Photo of a smiling male trainer in a blue t-shirt holding a tablet" style="left:0;top:220px;width:267px;height:240px;background:radial-gradient(ellipse at 55% 45%,#5d9ad8 0%,#3c77c0 30%,#e0b320 62%,#fbc813 85%);"></div>
    <svg class="overlay" width="267" height="564" viewBox="0 0 267 564">
      <path d="M0,410 C60,450 170,470 267,400 V564 H0 Z" fill="#ffffff"/>
      <path d="M0,440 C70,470 180,470 267,400 C200,480 80,495 0,470 Z" fill="#0b0b0b"/>
    </svg>
    <div class="brand brand--cover">JAB YARD</div>
    <h1 class="cover-heading">Get fit, lose weight<br><span>&amp; feel great</span></h1>
    <p class="price-bar">Unlimited outdoor boxing classes <span>$14.95</span></p>
    <p class="tagline">Complete affordability &amp; No judgements guaranteed</p>
    <p class="web">www.punchyard-fit.com.au</p>
  </div>
</section>

<!-- Inside of the trifold -->
<section class="spread spread--inside">
  <div class="photo" role="img" aria-label="Photo of a man and woman doing planks on grass in sunlight" style="left:0;top:230px;width:267px;height:334px;background:linear-gradient(180deg,#c9b98a 0%,#6f8a45 45%,#3f6a2a 100%);"></div>
  <div class="photo" role="img" aria-label="Light double exposure photo of a hooded boxer punching over a city skyline" style="left:267px;top:230px;width:533px;height:334px;background:radial-gradient(ellipse at 70% 45%,#8c8c8c 0%,#c4c4c4 30%,#ececec 60%,#ffffff 85%);"></div>

  <svg class="overlay" width="800" height="564" viewBox="0 0 800 564">
    <defs>
      <clipPath id="topBand">
        <path d="M0,0 H800 V150 C720,190 660,280 560,285 C470,290 400,260 330,262 C300,263 285,268 265,300 C235,335 200,300 150,270 C100,240 50,240 0,255 Z"/>
      </clipPath>
    </defs>
    <g clip-path="url(#topBand)">
      <rect x="0" y="0" width="267" height="564" fill="#0b0b0b"/>
      <rect x="267" y="0" width="266" height="564" fill="#fbc813"/>
      <rect x="533" y="0" width="267" height="564" fill="#0b0b0b"/>
    </g>
    <path d="M800,150 C720,190 660,280 560,285 C470,290 400,260 330,262 C300,263 285,268 265,300 C235,335 200,300 150,270 C100,240 50,240 0,255" fill="none" stroke="#fbc813" stroke-width="14"/>
  </svg>

  <div class="panel panel--1 on-dark">
    <div class="feature" style="top:22px;">
      <svg class="icon" viewBox="0 0 34 34"><circle cx="17" cy="17" r="15.5" fill="none" stroke="#fbc813" stroke-width="2"/><path d="M9,11 H25 M11,8 V14 M23,8 V14 M17,12 V20 M13,26 L17,20 L21,26" stroke="#fbc813" stroke-width="2" fill="none"/></svg>
      <h3 class="feature__title">Strengthen &amp; tone your core</h3>
      <p class="feature__text">You're core muscles are some of you're most important muscles. Each workout you do incorporates core exercises to help avoid injuries and make you're total body stronger</p>
    </div>
  </div>

  <div class="panel panel--2 on-yellow">
    <div class="feature" style="top:22px;">
      <svg class="icon" viewBox="0 0 34 34"><circle cx="17" cy="17" r="15.5" fill="none" stroke="#0b0b0b" stroke-width="2"/><path d="M8,12 V24 M8,20 H26 V24 M14,16 H25 V20" stroke="#0b0b0b" stroke-width="2" fill="none"/><circle cx="11" cy="17" r="1.8" fill="#0b0b0b"/></svg>
      <h3 class="feature__title">Sleep better</h3>
      <p class="feature__text">One of the best parts of exercise is the benefit it has on your sleeping patterns. Every class you do will have you filled with energy that will pump you up for the rest of your day and that night you'll sleep deeper &amp; more sound. Best of all you'll wake up feeling fitter and with more energy!</p>
    </div>
    <div class="contact contact--inside">
      <div class="contact__line"><svg viewBox="0 0 12 12"><circle cx="6" cy="6" r="5.2" fill="none" stroke="#d9a400" stroke-width="1.2"/><path d="M4,3.5 L5,3.5 L5.5,5 L4.8,5.6 C5.3,6.6 5.9,7.2 6.8,7.6 L7.4,6.9 L8.7,7.4 L8.5,8.5 C6,8.5 3.6,6 4,3.5 Z" fill="#d9a400"/></svg>0400 123 987</div>
      <div class="contact__line"><svg viewBox="0 0 12 12"><rect x="1.5" y="3" width="9" height="6" fill="none" stroke="#d9a400" stroke-width="1.1"/><path d="M1.5,3 L6,6.5 L10.5,3" fill="none" stroke="#d9a400" stroke-width="1.1"/></svg>info@punchyard-fit.com.au</div>
      <div class="contact__line"><svg viewBox="0 0 12 12"><circle cx="6" cy="6" r="4.8" fill="none" stroke="#d9a400" stroke-width="1.1"/><path d="M1.2,6 H10.8 M6,1.2 C3.8,4 3.8,8 6,10.8 M6,1.2 C8.2,4 8.2,8 6,10.8" fill="none" stroke="#d9a400" stroke-width="0.9"/></svg><span style="letter-spacing:2px;">www.punchyard-fit.com.au</span></div>
    </div>
  </div>

  <div class="panel panel--3 on-dark">
    <div class="feature" style="top:22px;">
      <svg class="icon" viewBox="0 0 34 34"><circle cx="17" cy="17" r="15.5" fill="none" stroke="#fbc813" stroke-width="2"/><circle cx="13" cy="10" r="2.5" fill="#fbc813"/><circle cx="21" cy="10" r="2.5" fill="#fbc813"/><path d="M13,14 V26 M21,14 V26 M10,16 H24" stroke="#fbc813" stroke-width="2.4" fill="none"/></svg>
      <h3 class="feature__title">Supportive environment</h3>
      <p class="feature__text">At JAB YARD you'll be surrounded by trainers &amp; other members who are there to encourage &amp; motivate you to reach your goals and to get you moving more</p>
    </div>
  </div>

  <div class="badge">Feel good<br>outdoor<br>boxing<br>classes</div>
</section>

</body>
</html>
```